Biography Landing Page for Trent Halby

We need a landing page design for the CEO of Granite Lantern (see GraniteLantern.com). We have a domains -
TrentHalby.com
TheKindestBakerOnTheRiverbend.com
TrentHalby.net
JdTrentHalby.com
JdTrentHalby.net

I will attached a color pallet for you to use. z

I am attaching the lengthy copy for the website. I look forward to seeing how you design this page. I recommend that there be options to expand / open copy for each of the major sections so the reader can see the headings and choose to open them to read more. But, be sure that the expanded sections are also designed.

I have a collection of photos to use for the site. We will slide those photos in later. For now, please leave lots of “for position only” spots for photos.

We will have lots of pictures to put on this site, but we will have those inserted later. For the design, please just use these few photos as placeholder

We will need all files in Figma Design (Desktop, Laptop, Mobile)

```html
<!DOCTYPE html>
<html lang="en">
<head>
<meta charset="utf-8">
<title>Trent Halby — Biography</title>
<link href="https://fonts.googleapis.com/css2?family=Cormorant+Garamond:wght@500;600;700&family=Inter:wght@400;500;600;700&display=swap" rel="stylesheet">
<style>
:root{
  --bg-top:#1a2440;
  --bg-mid:#0e1c3f;
  --bg-bottom:#101a38;
  --card:#16264b;
  --card-2:#1a2b52;
  --line:rgba(255,255,255,.09);
  --gold:#dcbc80;
  --gold-2:#c9a163;
  --text:#f2ede2;
  --muted:#b7bfd2;
  --dim:#7f8aa6;
  --red:#b3232e;
}
*{box-sizing:border-box;margin:0;padding:0}
html,body{width:1200px;height:4273px;overflow:hidden}
body{
  position:relative;
  background:
    radial-gradient(600px 500px at 1050px 520px,rgba(120,30,50,.25),transparent 70%),
    radial-gradient(700px 500px at 1100px 4200px,rgba(110,30,50,.25),transparent 70%),
    linear-gradient(180deg,var(--bg-top) 0,var(--bg-mid) 700px,var(--bg-mid) 3200px,var(--bg-bottom) 4273px);
  color:var(--text);
  font-family:"Inter",sans-serif;
}
.abs{position:absolute}
.wrap{left:146px;width:908px}

/* nav */
.brand{display:flex;align-items:center;gap:10px}
.brand-dot{width:14px;height:14px;border-radius:50%;background:var(--gold-2)}
.brand-name{font-family:"Inter",sans-serif;font-weight:600;font-size:15px;color:var(--text);letter-spacing:.02em;white-space:nowrap}
.nav{top:27px;right:146px;display:flex;gap:17px;font-size:9.5px;letter-spacing:.12em;color:var(--muted)}

/* shared */
.badge{display:inline-block;border:1px solid rgba(220,188,128,.4);border-radius:20px;padding:4px 10px;font-size:7.5px;letter-spacing:.16em;color:var(--gold);text-transform:uppercase}
.h2{font-family:"Cormorant Garamond",serif;font-weight:600;font-size:34px;line-height:36px;color:var(--text)}
.lede{font-size:11px;line-height:20px;color:var(--muted)}
.card{background:linear-gradient(180deg,var(--card-2),var(--card));border:1px solid var(--line);border-radius:12px;box-shadow:0 8px 22px rgba(0,0,0,.25)}
.btn{display:inline-flex;align-items:center;justify-content:center;height:30px;padding:0 16px;border-radius:16px;font-size:8.5px;font-weight:700;letter-spacing:.12em}
.btn-gold{background:linear-gradient(180deg,#e6c88e,#c9a163);color:#1b1a20}
.btn-ghost{border:1px solid rgba(255,255,255,.25);color:var(--text)}

/* hero */
.hero-title{font-family:"Cormorant Garamond",serif;font-weight:600;font-size:58px;line-height:56px;color:var(--text)}
.stats{display:flex;gap:8px}
.stat{width:152px;height:66px;padding:14px 12px}
.stat b{display:block;font-family:"Cormorant Garamond",serif;font-weight:600;font-size:22px;color:var(--gold);line-height:22px}
.stat span{font-size:7.5px;color:var(--muted)}
.hero-quote{font-family:"Cormorant Garamond",serif;font-size:21px;color:var(--gold)}
.portrait{left:714px;top:110px;width:288px;height:475px;border-radius:18px;background:rgba(40,50,80,.55);border:1px solid var(--line)}
.portrait-photo{position:absolute;left:20px;top:20px;width:248px;height:355px;border-radius:14px;background:linear-gradient(180deg,#5a5a63,#3c4056 60%,#2a3150);border:1px solid var(--line);display:flex;align-items:center;justify-content:center;font-size:9px;letter-spacing:.12em;color:#b8bccb}
.tag-red{position:absolute;right:14px;top:14px;background:var(--red);color:#fff;font-size:7px;letter-spacing:.14em;padding:4px 9px;border-radius:10px}
.portrait-name{position:absolute;left:16px;top:393px;width:256px;height:66px;border-radius:10px;background:#0f1a36;display:flex;align-items:center;gap:10px;padding:0 12px}
.portrait-name i{width:34px;height:34px;border-radius:50%;background:#3a3f52;flex:none}
.portrait-name b{display:block;font-family:"Cormorant Garamond",serif;font-weight:600;font-size:16px}
.portrait-name span{font-size:7.5px;color:var(--muted);line-height:10px;display:block}
.hero-rule{top:694px;left:0;width:1200px;height:1px;background:var(--line)}

/* snapshot */
.facts{display:grid;grid-template-columns:repeat(3,1fr);gap:13px}
.fact{height:62px;padding:16px 15px}
.fact small{display:block;font-size:6.5px;letter-spacing:.16em;color:var(--gold);margin-bottom:5px}
.fact b{font-size:12px;font-weight:700}

/* journey */
.step{height:80px;display:flex;align-items:center;padding:0 16px;gap:20px}
.step-num{width:38px;height:38px;border-radius:50%;background:linear-gradient(180deg,#e6c88e,#c9a163);color:#2a2218;font-family:"Cormorant Garamond",serif;font-weight:700;font-size:15px;display:flex;align-items:center;justify-content:center;flex:none}
.step h3{font-family:"Cormorant Garamond",serif;font-weight:600;font-size:19px;margin-bottom:6px}
.step p{font-size:10px;color:var(--muted)}
.metrics{display:grid;grid-template-columns:repeat(4,1fr);gap:14px}
.metric{height:80px;display:flex;flex-direction:column;align-items:center;justify-content:center}
.metric b{font-family:"Cormorant Garamond",serif;font-weight:600;font-size:22px;color:var(--gold)}
.metric span{font-size:7.5px;color:var(--muted);margin-top:3px}

/* highlights */
.highlights{display:grid;grid-template-columns:repeat(3,1fr);gap:13px}
.highlight{height:164px;padding:20px 17px}
.highlight em{font-style:normal;font-family:"Cormorant Garamond",serif;font-weight:600;font-size:20px;color:var(--gold)}
.highlight h3{font-family:"Cormorant Garamond",serif;font-weight:600;font-size:21px;margin:8px 0 6px}
.highlight p{font-size:10px;line-height:20px;color:var(--muted)}
.philosophy{font-family:"Cormorant Garamond",serif;font-size:22px;line-height:26px;color:var(--gold)}

/* photo grid */
.ph{position:absolute;border-radius:14px;border:1px solid var(--line);background:radial-gradient(200px 60px at 50% 0,rgba(255,255,255,.06),transparent),linear-gradient(180deg,#1d2c52,#15264a);display:flex;align-items:center;justify-content:center;font-size:9px;letter-spacing:.14em;color:var(--dim)}

/* values */
.value{position:absolute;padding:16px 14px}
.value h3{font-family:"Cormorant Garamond",serif;font-weight:600;font-size:20px;margin-bottom:8px}
.value p{font-size:10px;line-height:20px;color:var(--muted)}

/* cta */
.cta{left:332px;top:3874px;width:536px;height:259px;text-align:center;padding-top:36px}
.cta h2{font-family:"Cormorant Garamond",serif;font-weight:600;font-size:34px;margin:14px 0 8px}
.cta p{font-size:10.5px;line-height:20px;color:var(--muted);padding:0 26px}
.cta .btns{display:flex;gap:14px;justify-content:center;margin-top:18px}

.footer-note{right:146px;top:4226px;font-size:9px;color:var(--text)}
</style>
</head>
<body>

<!-- nav -->
<div class="abs brand" style="left:146px;top:25px">
  <span class="brand-dot"></span>
  <span class="brand-name">Trent Halby</span>
</div>
<nav class="abs nav"><span>PROFILE</span><span>STORY</span><span>HIGHLIGHTS</span><span>VALUES</span><span>CONTACT</span></nav>

<!-- hero -->
<div class="abs" style="left:146px;top:104px"><span class="badge">Founder • Entrepreneur • Patriot</span></div>
<h1 class="abs hero-title" style="left:146px;top:146px;width:460px">I Didn’t Just Learn From Failure — I Built My Empire From It.</h1>
<p class="abs lede" style="left:146px;top:388px;width:450px">William Trent Halby is a business leader, speaker, investor, and founder of Granite Lantern. Every setback became fuel. Every challenge became momentum. This page presents a life built on resilience, conviction, patriotism, and leadership.</p>
<div class="abs" style="left:146px;top:471px;display:flex;gap:12px">
  <span class="btn btn-gold">READ THE STORY</span><span class="btn btn-ghost">VIEW HIGHLIGHTS</span>
</div>
<div class="abs stats" style="left:146px;top:525px">
  <div class="card stat"><b>3</b><span>Multi-Million Dollar Exits</span></div>
  <div class="card stat"><b>2000+</b><span>Employees Led</span></div>
  <div class="card stat"><b>$500M</b><span>Strategic Partnership</span></div>
</div>
<p class="abs hero-quote" style="left:146px;top:620px">“Every ‘no’ became the combustion for a bigger ‘yes’.”</p>

<div class="abs portrait">
  <div class="portrait-photo" role="img" aria-label="Portrait photo of Trent Halby">MAIN PORTRAIT AREA</div>
  <span class="tag-red">PHOTO PLACEHOLDER</span>
  <div class="portrait-name"><i></i><div><b>William Trent Halby</b><span>CEO • Investor • Speaker • Association Executive</span></div></div>
</div>
<div class="abs hero-rule"></div>

<!-- snapshot -->
<div class="abs" style="left:146px;top:757px"><span class="badge">Quick Profile</span></div>
<h2 class="abs h2" style="left:146px;top:800px">The Executive Snapshot</h2>
<p class="abs lede" style="left:146px;top:845px;width:510px">A clean summary area you can keep as-is or edit later once the client finalizes all details and photography.</p>
<div class="abs wrap facts" style="top:906px">
  <div class="card fact"><small>FULL NAME</small><b>William Trent Halby</b></div>
  <div class="card fact"><small>KNOWN AS</small><b>Trent</b></div>
  <div class="card fact"><small>BIRTHPLACE</small><b>Indianapolis, Indiana</b></div>
  <div class="card fact"><small>CURRENT RESIDENCE</small><b>Austin, Texas</b></div>
  <div class="card fact"><small>PROFESSION</small><b>CEO, Speaker, Investor, Podcaster</b></div>
  <div class="card fact"><small>ORGANIZATION</small><b>Granite Lantern</b></div>
</div>

<!-- biography overview -->
<div class="abs" style="left:332px;top:1166px"><span class="badge">Biography Overview</span></div>
<h2 class="abs h2" style="left:332px;top:1208px;width:440px">A Life Defined by Defiance, Leadership, and Reinvention</h2>
<p class="abs lede" style="left:332px;top:1288px;width:510px">From early adversity to national business leadership, Trent Halby built a career by transforming setbacks into scale. His story spans entrepreneurship, healthcare, finance, advocacy, and the creation of Granite Lantern.</p>

<!-- journey -->
<div class="abs" style="left:146px;top:1471px"><span class="badge">Life Journey</span></div>
<h2 class="abs h2" style="left:146px;top:1512px;width:480px">From Early Adversity to National Influence</h2>
<div class="abs wrap" style="top:1607px;display:flex;flex-direction:column;gap:13px">
  <div class="card step"><span class="step-num">01</span><div><h3>Early Life</h3><p>Born into difficult circumstances, Halby’s earliest years were shaped by hardship, resilience, and a refusal to be defined by limitation.</p></div></div>
  <div class="card step"><span class="step-num">02</span><div><h3>Defying the Odds</h3><p>A life-threatening childhood accident became part of a larger story of perseverance, grit, and survival.</p></div></div>
  <div class="card step"><span class="step-num">03</span><div><h3>Identity and Restoration</h3><p>After decades of living with an imposed identity, he reclaimed his original name and reasserted his personal truth.</p></div></div>
  <div class="card step"><span class="step-num">04</span><div><h3>Business Growth</h3><p>From personal trainer to executive leader, Halby built and scaled multiple businesses across fitness, finance, and healthcare.</p></div></div>
</div>
<div class="abs wrap metrics" style="top:2088px">
  <div class="card metric"><b>12+</b><span>Major Facilities Built</span></div>
  <div class="card metric"><b>1M+</b><span>Square Feet Operated</span></div>
  <div class="card metric"><b>1000+</b><span>Sales Team Recruited</span></div>
  <div class="card metric"><b>Nationwide</b><span>Leadership &amp; Impact</span></div>
</div>

<!-- highlights -->
<div class="abs" style="left:146px;top:2291px"><span class="badge">Career Highlights</span></div>
<h2 class="abs h2" style="left:146px;top:2334px">Leadership, Scale, and Strategic Vision</h2>
<div class="abs wrap highlights" style="top:2392px">
  <div class="card highlight"><em>01</em><h3>Leadership at Scale</h3><p>Built high-growth organizations, led national teams, and scaled operations across multiple industries.</p></div>
  <div class="card highlight"><em>02</em><h3>Granite Lantern</h3><p>A platform centered on transparency, accountability, and empowering the Office of the Citizen.</p></div>
  <div class="card highlight"><em>03</em><h3>Patriotic Identity</h3><p>A personal brand rooted in faith, resilience, conviction, and a strong sense of national purpose.</p></div>
</div>

<!-- philosophy -->
<div class="abs" style="left:332px;top:2678px"><span class="badge">Core Philosophy</span></div>
<p class="abs philosophy" style="left:332px;top:2709px;width:560px">The credit belongs to the man who is actually in the arena — the one who strives, fails, dares greatly, and rises again.</p>

<!-- photo layout -->
<div class="abs" style="left:146px;top:2885px"><span class="badge">Photo Layout</span></div>
<h2 class="abs h2" style="left:146px;top:2928px">Image Placeholder Section</h2>
<p class="abs lede" style="left:146px;top:2973px;width:510px">This area gives you premium blocks for future biography photos, campaign-style images, and featured moments.</p>
<div class="ph" style="left:146px;top:3034px;width:329px;height:364px" role="img" aria-label="Featured biography photo">FEATURED IMAGE PLACEHOLDER</div>
<div class="ph" style="left:491px;top:3034px;width:274px;height:173px" role="img" aria-label="Biography photo">PHOTO PLACEHOLDER</div>
<div class="ph" style="left:779px;top:3034px;width:275px;height:173px" role="img" aria-label="Biography photo">PHOTO PLACEHOLDER</div>
<div class="ph" style="left:491px;top:3224px;width:563px;height:174px" role="img" aria-label="Wide campaign photo">WIDE PHOTO PLACEHOLDER</div>

<!-- values -->
<div class="abs" style="left:146px;top:3520px"><span class="badge">Core Values</span></div>
<h2 class="abs h2" style="left:146px;top:3562px;width:420px">Faith, Family, Resilience, and Responsibility</h2>
<p class="abs lede" style="left:146px;top:3644px;width:400px">Built on a belief in service, conviction, and personal responsibility, this personal brand narrative is designed to feel strong, polished, and deeply mission-driven.</p>
<div class="card value" style="left:589px;top:3519px;width:226px;height:101px"><h3>Faith</h3><p>Grounded in spiritual conviction and Biblical principles.</p></div>
<div class="card value" style="left:827px;top:3519px;width:227px;height:101px"><h3>Family</h3><p>Driven by loyalty, caregiving, and personal devotion.</p></div>
<div class="card value" style="left:589px;top:3632px;width:226px;height:121px"><h3>Resilience</h3><p>A life story shaped by endurance, restoration, and forward motion.</p></div>
<div class="card value" style="left:827px;top:3632px;width:227px;height:121px"><h3>Patriotism</h3><p>A strong identity tied to citizenship, accountability, and the American spirit.</p></div>

<!-- cta -->
<section class="abs card cta">
  <span class="badge">Call to Action</span>
  <h2>Join the Movement</h2>
  <p>Use this section for final call-to-action, social links, a lead capture form, or direct traffic to Granite Lantern.</p>
  <div class="btns"><span class="btn btn-gold">LEARN MORE</span><span class="btn btn-ghost">FOLLOW THE STORY</span></div>
</section>

<!-- footer -->
<div class="abs brand" style="left:146px;top:4220px">
  <span class="brand-dot"></span>
  <span class="brand-name">Trent Halby</span>
</div>
<p class="abs footer-note">Premium biography landing page concept with editable placeholders and expanded sections.</p>

</body>
</html>
```